Design Lumotab decals that are actually useful

Hi designers,

Have you ever wanted to design your own Lumotab breeze sticker/decal? Now's your chance. We want you to design a Lumotab decal that is actually useful!

Your task is to design a sticker or decal that would be useful and helpful for different types of professions. Think about what people doing different types of jobs would find useful on the exterior of their Lumotab.

Here are some examples of a few professions and what they might find useful:

- Student: periodic and multiplication tables, formula charts or world maps.
- Designer: colour charts, the golden ratio or a ruler.
- Ship Captain: map of world shipping routes.
- Zoologist / Vet: skeletal chart of common pets - dog, cat, bird or Guinea pig.
- Developer/Programmer: creative chart of common HTML code.
- Doctor: human anatomy chart.
- Other: visual steps showing you how to do various tie knots or hair styles.

Here are some other professions to keep you thinking:

Teacher
Banker
Accountant
Lawyer
Scientist / lab technician
Marine Biologist
Bookie
Journalist
CEO
Engineer
Filmmaker
Artist
Architect
Librarian
Firefighter
Pilot

Be creative - what do you think would be useful to have pasted on the exterior of your Lumotab?

In your submission please mention in the design description field, the profession your design is aiming to be useful or helpful for.

We can't wait to see what you think of. Have fun and good luck!

Cheers,
SketchHive

Reason: Dear designers, We are seeing some top designs being submitted - thanks to all designers who have submitted designs. We have decided to extend the contest by a week to give designers who have just seen the project more time to conceptualise and execute a design submission for the competition. You might be interested in a designer discussion we're holding about the brief components, so check that out and join in. Thanks Pam / Community Manager

Hello designers, SketchHive here :) We've seen your designs come through and just wanted to give you some more direction about the kind of designs we'd like to see. We've seen lots of occupation-inspired designs, that are just themed. But what we're really after is more of a helpful decal. Something people can look at or use in a situation that will actually make the laptop a useful tool when it is not operating as a laptop. So a decal with the periodic table, a decal with the multiplication table for students, a decal with pixelforge shortcuts for designers, a decal with the 2014 calendar. Please only submit useful Lumotab decals. Looking forward to seeing what you can design! Thanks, The SketchHive team.

Reason: Hi designers, extending the deadline for 1 more week to give designers maximum chance of submitting their best design ideas. - SketchHive

Target Market(s)

The target market is up to you, the only caveat is that the graphic is helpful or useful for your chosen audience.

Industry/Entity Type

Shipping

Requirements
Must have
• You can make the graphic the size of the exterior of a regular 13 or 15 inch (see http://www.lumora-devices.example/tab/ for hardware dimensions)

```html
<!DOCTYPE html>
<html lang="en">
<head>
<meta charset="utf-8">
<title>Lumotab Tool Shortcut Decal</title>
<link href="https://fonts.googleapis.com/css2?family=Questrial&display=swap" rel="stylesheet">
<style>
  :root{
    --page:#ffffff;
    --decal:#f2f2f4;
    --key:#ffffff;
    --ink:#2b2b2b;
    --red:#ec3138;
    --orange:#f2693a;
    --yellow:#f5e23a;
    --green:#5cc450;
    --brand:#c9c9cc;
  }
  html,body{margin:0;padding:0;overflow:hidden;background:var(--page);}
  .canvas{position:relative;width:1200px;height:1000px;overflow:hidden;font-family:"Questrial",sans-serif;color:var(--ink);}
  .decal{position:absolute;left:0;top:85px;width:1200px;height:830px;background:var(--decal);}
  .key{position:absolute;width:78px;height:78px;border-radius:14px;padding:4px;box-sizing:border-box;}
  .key--hot{background:linear-gradient(var(--red),var(--orange));}
  .key--warm{background:linear-gradient(var(--orange),var(--yellow));}
  .key--cool{background:linear-gradient(var(--yellow),var(--green));}
  .key__face{position:relative;width:100%;height:100%;background:var(--key);border-radius:10px;}
  .key__label{position:absolute;top:9px;left:0;right:0;text-align:center;font-size:8.5px;line-height:9px;}
  .key__letter{position:absolute;left:7px;bottom:4px;font-size:13px;}
  .key__icon{position:absolute;left:19px;top:22px;width:40px;height:40px;fill:none;stroke:var(--ink);stroke-width:1.4;}
  .brand{position:absolute;left:540px;top:488px;width:120px;text-align:center;font-size:22px;color:var(--brand);}
</style>
</head>
<body>
<div class="canvas">
  <div class="decal">
  </div>

  <div class="key key--hot" style="left:57px;top:404px"><div class="key__face"><span class="key__label">Select Tool</span><svg class="key__icon" viewBox="0 0 40 40"><path d="M14 6 L14 34 L20 27 L25 37 L29 35 L24 26 L33 25 Z"/></svg><span class="key__letter">A</span></div></div>

  <div class="key key--hot" style="left:149px;top:355px"><div class="key__face"><span class="key__label">Magic Wand</span><svg class="key__icon" viewBox="0 0 40 40"><path d="M16 8 L18 15 L25 13 L20 19 L24 25 L17 22 L12 27 L12 20 L6 16 L13 15 Z"/><path d="M21 22 L34 35 L32 37 L19 24"/></svg><span class="key__letter">W</span></div></div>
  <div class="key key--warm" style="left:149px;top:452px"><div class="key__face"><span class="key__label">Zoom Tool</span><svg class="key__icon" viewBox="0 0 40 40"><circle cx="17" cy="17" r="11"/><circle cx="17" cy="17" r="8"/><path d="M25 25 L34 34 L31 37 L22 28"/></svg><span class="key__letter">Z</span></div></div>

  <div class="key key--hot" style="left:251px;top:330px"><div class="key__face"><span class="key__label">Eraser</span><svg class="key__icon" viewBox="0 0 40 40"><path d="M4 22 L14 12 L36 12 L26 22 Z M4 22 L4 32 L26 32 L26 22 M26 32 L36 22 L36 12"/></svg><span class="key__letter">E</span></div></div>
  <div class="key key--warm" style="left:251px;top:432px"><div class="key__face"><span class="key__label">Clone Stamp</span><svg class="key__icon" viewBox="0 0 40 40"><circle cx="20" cy="10" r="5"/><path d="M20 15 L20 26 M8 26 L32 26 L32 34 L8 34 Z"/></svg><span class="key__letter">S</span></div></div>
  <div class="key key--cool" style="left:251px;top:530px"><div class="key__face"><span class="key__label">Crop Tool</span><svg class="key__icon" viewBox="0 0 40 40" style="stroke-width:2"><path d="M12 4 L12 30 L38 30 M4 12 L30 12 L30 38 M14 28 L28 14 M16 14 L28 14 L28 26"/></svg><span class="key__letter">C</span></div></div>

  <div class="key key--hot" style="left:354px;top:355px"><div class="key__face"><span class="key__label">Rotate View</span><svg class="key__icon" viewBox="0 0 40 40"><path d="M10 24 L10 14 M14 26 L14 10 M18 26 L18 9 M22 26 L22 12 M8 26 C8 34 12 38 20 38 C28 38 30 32 32 24"/><rect x="23" y="12" width="10" height="12" fill="#2b2b2b" transform="rotate(20 28 18)"/><path d="M18 6 C24 2 32 4 36 10 M33 9 L36 10 L36 6"/></svg><span class="key__letter">R</span></div></div>
  <div class="key key--warm" style="left:356px;top:449px"><div class="key__face"><span class="key__label">Gradient Tool</span><svg class="key__icon" viewBox="0 0 40 40" style="stroke:none"><defs><linearGradient id="grad-fill"><stop offset="0" stop-color="#1a1a1a"/><stop offset="1" stop-color="#ffffff"/></linearGradient></defs><rect x="2" y="6" width="38" height="28" fill="url(#grad-fill)"/></svg><span class="key__letter">G</span></div></div>

  <div class="key key--hot" style="left:457px;top:330px"><div class="key__face"><span class="key__label">Type Tool</span><svg class="key__icon" viewBox="0 0 40 40" style="stroke:none"><text x="20" y="36" text-anchor="middle" font-family="serif" font-size="38" fill="#2b2b2b">T</text></svg><span class="key__letter">T</span></div></div>
  <div class="key key--warm" style="left:457px;top:428px"><div class="key__face"><span class="key__label">Move Tool</span><svg class="key__icon" viewBox="0 0 40 40"><path d="M8 10 L8 30 L13 25 L22 24 Z"/><path d="M30 20 L30 38 M21 29 L39 29 M28 22 L30 20 L32 22 M28 36 L30 38 L32 36 M23 27 L21 29 L23 31 M37 27 L39 29 L37 31" stroke-width="2"/></svg><span class="key__letter">V</span></div></div>

  <div class="key key--hot" style="left:562px;top:355px"><div class="key__face"><span class="key__label">History Brush</span><svg class="key__icon" viewBox="0 0 40 40"><path d="M8 24 C8 10 30 8 34 22 C36 30 30 36 24 36"/><path d="M6 30 C10 36 18 36 20 30 C22 26 18 24 14 26 C10 28 10 32 6 30 Z M20 28 L36 10"/></svg><span class="key__letter">Y</span></div></div>

  <div class="brand">Lumotab</div>

  <div class="key key--hot" style="left:665px;top:330px"><div class="key__face"><span class="key__label">Shape Tool</span><svg class="key__icon" viewBox="0 0 40 40"><rect x="4" y="6" width="32" height="28"/></svg><span class="key__letter">U</span></div></div>
  <div class="key key--warm" style="left:665px;top:428px"><div class="key__face"><span class="key__label">Brush Tool</span><svg class="key__icon" viewBox="0 0 40 40"><path d="M4 30 C10 38 22 38 24 30 C26 24 20 22 16 24 C10 27 10 32 4 30 Z M22 26 L38 8 M24 29 L40 12"/></svg><span class="key__letter">B</span></div></div>

  <div class="key key--hot" style="left:768px;top:355px"><div class="key__face"><span class="key__label">Eyedropper</span><svg class="key__icon" viewBox="0 0 40 40"><path d="M24 10 L32 18" stroke-width="6"/><path d="M26 18 L12 32 L8 36 L6 34 L10 30 L22 14 Z" fill="#2b2b2b"/></svg><span class="key__letter">I</span></div></div>
  <div class="key key--warm" style="left:768px;top:452px"><div class="key__face"><span class="key__label" style="text-align:left;left:8px;top:6px">Spot Healing<br>Brush</span><svg class="key__icon" viewBox="0 0 40 40" style="top:26px"><path d="M10 12 C2 18 2 32 10 36" stroke-dasharray="2 2"/><rect x="14" y="10" width="12" height="28" rx="6" transform="rotate(40 20 24)"/><path d="M14 26 L26 22"/></svg><span class="key__letter">J</span></div></div>

  <div class="key key--hot" style="left:870px;top:330px"><div class="key__face"><span class="key__label">Dodge Tool</span><svg class="key__icon" viewBox="0 0 40 40"><circle cx="17" cy="16" r="11" fill="#2b2b2b"/><path d="M24 24 L34 34" stroke-width="3"/></svg><span class="key__letter">O</span></div></div>
  <div class="key key--warm" style="left:870px;top:428px"><div class="key__face"><span class="key__label">Slice Tool</span><svg class="key__icon" viewBox="0 0 40 40"><path d="M26 4 L40 4 L30 14 L24 12 Z" fill="#2b2b2b"/><path d="M24 12 L30 14 L10 34 L6 36 L8 30 Z"/></svg><span class="key__letter">K</span></div></div>
  <div class="key key--cool" style="left:870px;top:526px"><div class="key__face"><svg class="key__icon" viewBox="0 0 40 40" style="top:20px;left:20px;width:42px;height:42px"><path d="M6 4 L36 4 L36 28 L28 36 L6 36 Z M28 36 L28 28 L36 28 M12 12 L30 12 M12 16 L30 16 M12 20 L30 20 M12 24 L24 24"/></svg><span class="key__letter" style="top:6px;bottom:auto">N</span></div></div>

  <div class="key key--hot" style="left:974px;top:355px"><div class="key__face"><span class="key__label">Pen Tool</span><svg class="key__icon" viewBox="0 0 40 40"><path d="M8 36 L12 20 L28 8 L36 16 L24 32 Z M8 36 L18 26"/><rect x="17" y="22" width="4" height="4" fill="#2b2b2b"/><path d="M30 6 L38 14"/></svg><span class="key__letter">P</span></div></div>
  <div class="key key--warm" style="left:976px;top:452px"><div class="key__face"><span class="key__label">Marquee</span><svg class="key__icon" viewBox="0 0 40 40"><rect x="6" y="8" width="32" height="28" stroke-dasharray="6 5"/></svg><span class="key__letter">M</span></div></div>

  <div class="key key--hot" style="left:1073px;top:404px"><div class="key__face"><span class="key__label">Lasso Tool</span><svg class="key__icon" viewBox="0 0 40 40"><path d="M6 10 L16 18 L32 6 L30 24 L14 34 Z"/><circle cx="14" cy="30" r="3"/><path d="M14 33 C12 38 8 38 6 36"/></svg><span class="key__letter">L</span></div></div>
</div>
</body>
</html>
```